Ironpeak MMA - Ironpeak Path - 7-5-4

This will be for a wall logo. Probably printed on vinyl to adhere to the wall. This a rough draft concept of the project, but we're certainly open to other designs. Red, Black and White are the main colors we would like to use. The triangle motif is important, it denotes stability and base, which are important in jiu jistu.
The Ironpeak Path (7-5-4)
7 Virtues of a Warrior (Bushido)
R Rectitude
Doing what is right w/o regard for the consequences
C Courage
Inner strength to resist opposition. Courage not just to step on the mat but to make the right decisions
B Benevolence
Mindset to do good. Be kind and generous
P Politeness
Proper consideration and courtesy to others
L Loyalty
Faithfulness & Alliance. Not blind allegiance
H Honesty / Sincerity
Be a man of your word. Do what you say you will
Genuine Integrity in character & action
H Honor
Profound respect & ethical conduct
Make the right decisions to be worthy of respectability
5 Keys to Health
Nutrition - Eat sensibly
Exercise - Stay fit and ready
Rest - Recovery and Recharge
Hygiene - Stay Clean
Attitude - Assume positive intent
Look at life in a positive way
4 States of Mind (Spirit of Budo)
Shoshin - Beginners Mind
Be open to new ideas
Eager to Learn
Zanshin – Remaining Mind
Being Alert and Aware, but relaxed
Be Prepared
Mushin – No Mind (Clear Mind)
Be able to act in the moment without having to think
Fudoshin – Immovable Mind
Emotional Balance
Free from anger, fear, & doubt

```html
<!DOCTYPE html>
<html lang="en">
<head>
<meta charset="utf-8">
<title>Ironpeak Path 7-5-4</title>
<link rel="stylesheet" href="https://fonts.googleapis.com/css2?family=Figtree:wght@400;500;600;700&display=swap">
<style>
  :root {
    --red: #8c1711;
    --black: #1b1b1b;
    --grey-light: #e8e8e8;
    --grey-mid: #dcdcdc;
    --white: #ffffff;
    --ink: #111111;
    --rule: #d8d8d8;
  }
  html, body { margin: 0; padding: 0; overflow: hidden; background: var(--white); }
  .poster { width: 1200px; height: 1149px; display: block; font-family: "Figtree", sans-serif; }
  .title { font-size: 84px; font-weight: 500; fill: var(--ink); }
  .code { font-size: 76px; font-weight: 700; fill: var(--red); }
  .virtue { font-size: 30px; font-weight: 700; fill: var(--white); letter-spacing: 1px; }
  .virtue-dark { font-size: 30px; font-weight: 700; fill: var(--ink); letter-spacing: 1px; }
  .motto { font-size: 18px; font-weight: 500; fill: var(--white); }
  .motto-dark { font-size: 18px; font-weight: 500; fill: var(--ink); }
  .list-head { font-size: 29px; font-weight: 700; fill: var(--red); }
  .list-item { font-size: 22px; font-weight: 400; fill: var(--ink); }
  .list-item tspan.key { font-weight: 500; }
  .list-note { font-size: 17px; font-weight: 400; fill: #222; }
  .brand-name { font-size: 34px; font-weight: 700; fill: var(--red); letter-spacing: 1px; }
</style>
</head>
<body>
<svg class="poster" viewBox="0 0 1384 1326" width="1200" height="1149" xmlns="http://www.w3.org/2000/svg">

  <g class="frame" stroke="var(--rule)" stroke-width="2" fill="none">
    <line x1="360" y1="130" x2="120" y2="580"/>
    <line x1="1050" y1="130" x2="1290" y2="580"/>
  </g>

  <text class="title" x="700" y="165" text-anchor="middle">Ironpeak Path</text>
  <text class="code" x="720" y="254" text-anchor="middle">7-5-4</text>

  <g class="bands">
    <polygon class="band-loyalty" points="350,393 478,398 700,795 645,905" fill="var(--grey-light)"/>
    <polygon class="band-courage" points="1075,400 1190,400 772,1100 700,1025" fill="var(--grey-mid)"/>
    <polygon class="band-honesty" points="885,512 1000,512 700,1025 645,905" fill="var(--red)"/>
    <polygon class="band-politeness" points="478,400 1078,400 1022,497 535,497" fill="var(--black)"/>
    <polygon class="band-benevolence" points="275,293 345,392 698,1025 652,1105 220,393" fill="var(--black)"/>
    <polygon class="band-rectitude" points="290,293 1132,293 1187,390 345,390" fill="var(--red)"/>
  </g>

  <text class="virtue" x="383" y="356">RECTITUDE</text>
  <text class="motto" x="680" y="334">Doing what is right w/o regard for the</text>
  <text class="motto" x="680" y="364">consequences</text>

  <text class="virtue" x="806" y="458">POLITENESS</text>
  <text class="motto" x="765" y="440" text-anchor="end">Proper consideration</text>
  <text class="motto" x="765" y="472" text-anchor="end">&amp; courtesy to others</text>

  <text class="virtue-dark" x="709" y="576" text-anchor="middle">HONOR</text>
  <text class="motto-dark" x="707" y="613" text-anchor="middle">Act with</text>
  <text class="motto-dark" x="707" y="647" text-anchor="middle">honor and earn</text>
  <text class="motto-dark" x="709" y="681" text-anchor="middle">respect.</text>

  <text class="virtue" x="262" y="398" transform="rotate(62 262 398)">BENEVOLENCE</text>
  <text class="motto" x="466" y="698" transform="rotate(62 466 698)">Mindset to do good. Be kind and</text>
  <text class="motto" x="440" y="712" transform="rotate(62 440 712)">generous</text>

  <text class="motto-dark" x="462" y="466" transform="rotate(62 462 466)">Faithfulness &amp; Alliance.</text>
  <text class="motto-dark" x="446" y="503" transform="rotate(62 446 503)">Not blind allegiance</text>
  <text class="virtue-dark" x="568" y="698" transform="rotate(62 568 698)">LOYALTY</text>

  <text class="virtue-dark" x="1013" y="620" transform="rotate(-59 1013 620)">COURAGE</text>
  <text class="motto-dark" x="810" y="945" transform="rotate(-59 810 945)">Inner strength to face challenges and</text>
  <text class="motto-dark" x="922" y="812" transform="rotate(-59 922 812)">choose what’s right.</text>

  <text class="motto" x="790" y="765" transform="rotate(-59 790 765)">Keep your word and act</text>
  <text class="motto" x="818" y="778" transform="rotate(-59 818 778)">with integrity.</text>
  <text class="virtue" x="672" y="943" transform="rotate(-59 672 943)">HONESTY /</text>
  <text class="virtue" x="706" y="963" transform="rotate(-59 706 963)">SINCERITY</text>

  <g class="health">
    <text class="list-head" x="145" y="757">5 Keys to Health</text>
    <text class="list-item" x="160" y="806"><tspan class="key">Nutrition -</tspan> Eat sensibly</text>
    <text class="list-item" x="123" y="856"><tspan class="key">Exercise -</tspan> Stay fit and ready</text>
    <text class="list-item" x="129" y="906"><tspan class="key">Rest -</tspan> Recovery and Recharge</text>
    <text class="list-item" x="249" y="955"><tspan class="key">Hygiene -</tspan> Stay Clean</text>
    <text class="list-item" x="160" y="1007"><tspan class="key">Attitude -</tspan> Assume positive intent</text>
    <text class="list-item" x="240" y="1060">Look at life in a positive way</text>
  </g>

  <g class="mind">
    <text class="list-head" x="1015" y="757">4 States of Mind</text>
    <text class="list-item" x="988" y="800">Shoshin – Beginner’s Mind</text>
    <text class="list-note" x="988" y="830">Stay open and eager to learn.</text>
    <text class="list-item" x="962" y="877">Zanshin – Remaining Mind</text>
    <text class="list-note" x="960" y="907">Be calm, aware, and ready.</text>
    <text class="list-item" x="927" y="954">Mushin – No Mind</text>
    <text class="list-note" x="925" y="984">Act freely without hesitation.</text>
    <text class="list-item" x="900" y="1031">Fudoshin – Immovable Mind</text>
    <text class="list-note" x="898" y="1061">Stay balanced and unshaken.</text>
  </g>

  <g class="brand">
    <circle cx="580" cy="1162" r="10" fill="var(--red)"/>
    <text class="brand-name" x="602" y="1174">Ironpeak MMA</text>
  </g>
</svg>
</body>
</html>
```